Poster for a series of live music events

Looking for a simplistic poster design for live music gigs. I would like something that i can reuse by moving the positioning of the words on the poster and the colour scheme. Attached is an example of a design that i like. The size should be A4.
File format preferred would be photoshop.
Text in the poster is not that important at this stage as it is just a template i am after. But it should include band names, location, date and time. So feel free to make up the text. The file provided in the brief will show you the similar things that will be included.
Events

```html
<!DOCTYPE html>
<html lang="en">
<head>
<meta charset="utf-8">
<title>Live Music Night Poster</title>
<link rel="stylesheet" href="https://fonts.googleapis.com/css2?family=Righteous&family=Quicksand:wght@500;700&display=swap">
<style>
  :root {
    --ink: #000000;
    --cyan: #5ee9e2;
    --mint: #6ff0a8;
    --lime: #7dff45;
    --display: "Righteous", sans-serif;
    --body: "Quicksand", sans-serif;
  }
  html, body {
    margin: 0;
    padding: 0;
    overflow: hidden;
    background: var(--ink);
  }
  .poster {
    position: relative;
    width: 848px;
    height: 1200px;
    overflow: hidden;
    background: var(--ink);
  }
  .poster-art {
    position: absolute;
    inset: 0;
    display: block;
  }
  .venue-name {
    font-family: var(--body);
    font-weight: 700;
    font-size: 52px;
    fill: var(--cyan);
  }
  .event-date {
    font-family: var(--display);
    font-size: 30px;
    fill: var(--cyan);
  }
  .band {
    font-family: var(--display);
    fill: url(#lineup-tint);
  }
  .info {
    font-family: var(--display);
    font-size: 24px;
    fill: var(--lime);
  }
  .address {
    font-family: var(--body);
    font-weight: 500;
    font-size: 20px;
    fill: var(--lime);
  }
</style>
</head>
<body>
<main class="poster">
  <svg class="poster-art" width="848" height="1200" viewBox="0 0 848 1200" xmlns="http://www.w3.org/2000/svg">
    <defs>
      <linearGradient id="lineup-tint" gradientUnits="userSpaceOnUse" x1="110" y1="320" x2="730" y2="960">
        <stop offset="0" stop-color="#5ee9e2"/>
        <stop offset="0.55" stop-color="#6ff0a8"/>
        <stop offset="1" stop-color="#7dff45"/>
      </linearGradient>
      <linearGradient id="edge-tint" x1="0" y1="0" x2="0" y2="1">
        <stop offset="0" stop-color="#5ee9e2"/>
        <stop offset="1" stop-color="#7dff45"/>
      </linearGradient>
      <radialGradient id="splash-cyan" cx="0.5" cy="0.5" r="0.5">
        <stop offset="0" stop-color="#5ee9e2" stop-opacity="0.85"/>
        <stop offset="1" stop-color="#5ee9e2" stop-opacity="0"/>
      </radialGradient>
      <radialGradient id="splash-lime" cx="0.5" cy="0.5" r="0.5">
        <stop offset="0" stop-color="#7dff45" stop-opacity="0.85"/>
        <stop offset="1" stop-color="#7dff45" stop-opacity="0"/>
      </radialGradient>
    </defs>

    <!-- side edges -->
    <rect class="edge edge--left" x="0" y="0" width="26" height="1200" fill="url(#edge-tint)" role="img" aria-label="Zigzag border edge"/>
    <rect class="edge edge--right" x="822" y="0" width="26" height="1200" fill="url(#edge-tint)" role="img" aria-label="Zigzag border edge"/>

    <!-- header artwork -->
    <rect class="notes notes--left" x="30" y="10" width="220" height="180" rx="40" fill="url(#splash-cyan)" role="img" aria-label="Floating music notes and treble clef"/>
    <rect class="notes notes--right" x="600" y="10" width="220" height="140" rx="40" fill="url(#splash-cyan)" role="img" aria-label="Floating music notes"/>
    <ellipse class="notes notes--burst" cx="425" cy="140" rx="170" ry="120" fill="url(#splash-cyan)" role="img" aria-label="Burst of music notes behind the venue name"/>

    <text class="venue-name" x="424" y="182" text-anchor="middle">loudhouse</text>

    <!-- date rule -->
    <g class="date-rule" fill="var(--cyan)" stroke="var(--cyan)">
      <line x1="120" y1="305" x2="305" y2="305" stroke-width="3"/>
      <line x1="520" y1="305" x2="712" y2="305" stroke-width="3"/>
      <circle cx="120" cy="305" r="7" stroke="none"/>
      <circle cx="712" cy="305" r="7" stroke="none"/>
    </g>
    <text class="event-date" x="412" y="316" text-anchor="middle">06.05.2015</text>

    <!-- lineup -->
    <g class="lineup">
      <text class="band" x="115" y="415" font-size="105" textLength="390" lengthAdjust="spacingAndGlyphs">RUNNING</text>
      <rect class="pattern" x="520" y="342" width="200" height="62" fill="url(#lineup-tint)" opacity="0.8" role="img" aria-label="Zigzag line pattern"/>
      <rect class="pattern" x="115" y="426" width="375" height="58" fill="url(#lineup-tint)" opacity="0.8" role="img" aria-label="Stacked dash pattern"/>
      <text class="band" x="500" y="490" font-size="90" textLength="218" lengthAdjust="spacingAndGlyphs">AWAY</text>

      <text class="band" x="115" y="596" font-size="110" textLength="385" lengthAdjust="spacingAndGlyphs">JERSEY</text>
      <text class="band" x="505" y="596" font-size="118" textLength="215" lengthAdjust="spacingAndGlyphs">girls</text>
      <rect class="pattern" x="240" y="612" width="250" height="22" fill="url(#lineup-tint)" opacity="0.8" role="img" aria-label="Wavy line pattern"/>
      <rect class="pattern" x="570" y="602" width="150" height="38" fill="url(#lineup-tint)" opacity="0.8" role="img" aria-label="Wavy line pattern"/>

      <circle class="ampersand-badge" cx="198" cy="680" r="44" fill="url(#lineup-tint)" role="img" aria-label="Ampersand with treble clef"/>
      <text class="band" x="248" y="718" font-size="104" textLength="226" lengthAdjust="spacingAndGlyphs">TOP</text>
      <text class="band" x="478" y="718" font-size="104" textLength="242" lengthAdjust="spacingAndGlyphs">HAT</text>
      <rect class="pattern" x="115" y="732" width="355" height="38" fill="url(#lineup-tint)" opacity="0.8" role="img" aria-label="Zigzag band pattern"/>
      <text class="band" x="475" y="787" font-size="96" textLength="245" lengthAdjust="spacingAndGlyphs">SATIN</text>

      <text class="band" x="115" y="868" font-size="86" textLength="345" lengthAdjust="spacingAndGlyphs">NEVER</text>
      <text class="band" x="555" y="864" font-size="54" textLength="165" lengthAdjust="spacingAndGlyphs">ON A</text>
      <rect class="pattern" x="115" y="882" width="240" height="58" fill="url(#lineup-tint)" opacity="0.8" role="img" aria-label="Stacked dash pattern"/>
      <text class="band" x="368" y="940" font-size="92" textLength="352" lengthAdjust="spacingAndGlyphs">SUNDAY</text>

      <rect class="lineup-rule" x="115" y="946" width="607" height="5" fill="var(--lime)"/>
    </g>

    <!-- entry details -->
    <text class="info" x="115" y="992">10 enrty</text>
    <text class="info" x="720" y="992" text-anchor="end">Doors: 8 pm</text>

    <!-- footer -->
    <ellipse class="notes notes--footer" cx="425" cy="1080" rx="180" ry="60" fill="url(#splash-lime)" role="img" aria-label="Burst of music notes"/>
    <g class="footer-rule" fill="var(--lime)" stroke="var(--lime)">
      <line x1="120" y1="1130" x2="712" y2="1130" stroke-width="3"/>
      <circle cx="120" cy="1130" r="7" stroke="none"/>
      <circle cx="712" cy="1130" r="7" stroke="none"/>
    </g>
    <text class="address" x="412" y="1176" text-anchor="middle">123 Address St.  •  City,  •  888-888-8888</text>
  </svg>
</main>
</body>
</html>
```